New Web Design Project for kitchen company

We need a homepage mockup for a company that sells and installs kitchen and baths. Use your creative talent to come up with something visually appeal and professional for this web-site.

Please see the attached brief.

If you have any questions feel free to post them right on the project discussion.

Target Market(s)

homeowners

Number of Pages Required

1 page

Font styles to use
Serif
Other font styles liked:
• Something similar to the logo

```html
<!DOCTYPE html>
<html lang="en">
<head>
<meta charset="utf-8">
<title>Harborline Kitchen and Bath</title>
<link rel="stylesheet" href="https://fonts.googleapis.com/css2?family=Marcellus&family=Montserrat:wght@400;500&family=Open+Sans:wght@400;600&display=swap">
<style>
:root{
  --ink:#111111;
  --text:#333333;
  --muted:#555555;
  --panel:#f4f4f4;
  --field:#ffffff;
  --line:#222222;
  --white:#ffffff;
  --star:#f2a71b;
  --footer:#000000;
}
*{box-sizing:border-box;margin:0;padding:0}
html,body{width:1200px;height:3276px;overflow:hidden;background:var(--white)}
body{position:relative;font-family:"Open Sans",sans-serif;color:var(--text)}
.abs{position:absolute}
.serif{font-family:"Marcellus",serif;color:var(--ink)}
.sans{font-family:"Montserrat",sans-serif}
.btn{position:absolute;display:flex;align-items:center;justify-content:center;border:2px solid var(--line);border-radius:20px;font-family:"Montserrat",sans-serif;font-size:13px;color:var(--ink);background:transparent}
.photo{position:absolute}
.section-title{position:absolute;left:0;width:1200px;text-align:center;font-family:"Marcellus",serif;font-size:36px;color:var(--ink)}
.rule{position:absolute;height:2px;width:38px;background:var(--ink)}

/* header */
.brand{left:74px;top:22px;display:flex;align-items:center;gap:12px}
.brand-mark{width:64px;height:64px;border:3px solid var(--ink);border-radius:50%}
.brand-name{font-family:"Marcellus",serif;color:var(--ink);font-size:26px;line-height:1}
.brand-sub{font-family:"Marcellus",serif;color:var(--ink);font-size:14px;line-height:1.1}
.brand-tag{font-family:"Marcellus",serif;color:var(--ink);font-size:8px;letter-spacing:3px}
.nav a{position:absolute;top:50px;font-family:"Montserrat",sans-serif;font-size:13px;color:var(--ink);text-decoration:none}
.nav .active{border-bottom:1px solid var(--ink);padding-bottom:9px;font-weight:500}

/* hero */
.hero{left:0;top:125px;width:1200px;height:602px;background:linear-gradient(100deg,#6b6c6a 0%,#a59e94 35%,#8b8176 60%,#4a3a30 100%)}
.hero-text{left:0;width:1200px;text-align:center;color:var(--white)}
.dot{position:absolute;width:7px;height:7px;border-radius:50%;background:rgba(255,255,255,.55)}

/* services */
.card{position:absolute;top:833px;width:318px;height:413px;background:var(--panel)}
.card.raised{box-shadow:0 2px 8px rgba(0,0,0,.18)}
.card .photo{left:10px;top:9px;width:298px;height:215px}
.card .badge{position:absolute;left:136px;top:203px;width:46px;height:46px;border-radius:50%;background:var(--white)}
.card h3{position:absolute;top:246px;width:100%;text-align:center;font-family:"Marcellus",serif;font-weight:400;font-size:17px;color:var(--ink)}
.card .rule{left:140px;top:275px}
.card p{position:absolute;left:22px;width:274px;top:286px;text-align:center;font-size:11px;line-height:15px;color:var(--muted)}
.card .btn{left:86px;top:355px;width:146px;height:36px}

/* projects */
.overlay{background:rgba(40,40,40,.82)}

/* about */
.frame{position:absolute;border:2px solid #555}
.about-p{position:absolute;left:627px;width:462px;font-size:11.5px;line-height:15px;color:var(--text)}

/* quote */
.field{position:absolute;background:var(--field);font-family:"Open Sans",sans-serif;font-size:12px;color:var(--ink);padding:14px 12px}

/* footer */
.footer-h{position:absolute;top:3010px;font-family:"Marcellus",serif;font-size:15px;color:var(--white)}
.footer-rule{position:absolute;top:3036px;width:38px;height:1px;background:var(--white)}
.flink{position:absolute;left:458px;font-family:"Montserrat",sans-serif;font-size:13px;color:var(--white)}
.flink span{margin-right:14px}
.fline{position:absolute;left:673px;font-size:13px;color:var(--white)}
.social{position:absolute;top:3223px;width:23px;height:23px;border-radius:50%;background:var(--white)}
</style>
</head>
<body>

<!-- header -->
<div class="abs brand">
  <div class="brand-mark"></div>
  <div>
    <div class="brand-name">HARBORLINE</div>
    <div class="brand-sub">KITCHEN AND BATH, INC</div>
    <div class="brand-tag">COMMITTED TO QUALITY</div>
  </div>
</div>
<nav class="nav">
  <a class="active" style="left:500px">Home</a>
  <a style="left:571px">About us</a>
  <a style="left:658px">Our Services</a>
  <a style="left:764px">Projects</a>
  <a style="left:850px">Contact us</a>
</nav>
<div class="btn" style="left:958px;top:39px;width:129px;height:36px">Get a Quote</div>

<!-- hero -->
<div class="photo hero" role="img" aria-label="Bright white kitchen with stainless ovens, pendant lights and bar stools"></div>
<div class="abs hero-text serif" style="top:360px;font-size:19px;color:var(--white)">Welcome to</div>
<div class="abs hero-text serif" style="top:382px;font-size:38px;color:var(--white)">Harborline Kitchen and Bath</div>
<div class="abs hero-text" style="top:429px;font-size:12.5px;line-height:15px">Lorem Ipsum simply dummy text of the printing and typesetting industry<br>in the industry's standard dummy text ever since the 1500s,</div>
<div class="btn" style="left:522px;top:475px;width:154px;height:36px;background:var(--ink);border-color:var(--ink);color:var(--white)">Read More</div>
<div class="dot" style="left:578px;top:652px;background:var(--white)"></div>
<div class="dot" style="left:591px;top:652px"></div>
<div class="dot" style="left:604px;top:652px"></div>
<div class="dot" style="left:617px;top:652px"></div>
<svg class="abs" style="left:0;top:640px" width="1200" height="90" viewBox="0 0 1200 90">
  <path d="M0 90 L0 55 C250 20 450 25 650 45 C850 65 1050 60 1200 20 L1200 90 Z" fill="#e6e6e6"/>
  <path d="M0 90 L0 65 C250 28 450 32 650 52 C850 72 1050 70 1200 40 L1200 90 Z" fill="#ffffff"/>
</svg>

<!-- services -->
<h2 class="section-title" style="top:760px;font-weight:400">Our Services</h2>
<div class="rule" style="left:581px;top:810px"></div>

<div class="card" style="left:103px">
  <div class="photo" role="img" aria-label="White kitchen with grey tile backsplash and a yellow kettle" style="background:linear-gradient(135deg,#d9dcdf,#9ea6ae 60%,#6e747a)"></div>
  <div class="badge"></div>
  <h3>Kitchen Design</h3>
  <div class="rule"></div>
  <p>Lorem Ipsum is simply dummy text of the printing and typesetting industry it has been the industry's dummy text ever since the 1500s,</p>
  <div class="btn">Read More</div>
</div>
<div class="card raised" style="left:442px">
  <div class="photo" role="img" aria-label="Bathroom with freestanding tub beneath windows" style="background:linear-gradient(135deg,#8f7a55,#d8cdb8 55%,#f1ede4)"></div>
  <div class="badge"></div>
  <h3>Bath Design</h3>
  <div class="rule"></div>
  <p>Lorem Ipsum is simply dummy text of the printing and typesetting industry it has been the industry's dummy text ever since the 1500s,</p>
  <div class="btn">Read More</div>
</div>
<div class="card" style="left:779px">
  <div class="photo" role="img" aria-label="Installer fitting a corner whirlpool tub" style="background:linear-gradient(135deg,#cfd3d6,#eceeef 55%,#7d7468)"></div>
  <div class="badge"></div>
  <h3>Installation Firm</h3>
  <div class="rule"></div>
  <p>Lorem Ipsum is simply dummy text of the printing and typesetting industry it has been the industry's dummy text ever since the 1500s,</p>
  <div class="btn">Read More</div>
</div>

<!-- projects -->
<h2 class="section-title" style="top:1313px;font-weight:400">Our Projects</h2>
<div class="photo" role="img" aria-label="Freestanding tub beside a potted palm" style="left:0;top:1382px;width:282px;height:215px;background:linear-gradient(135deg,#6d6a62,#a9a49a 55%,#d9cfc6)"></div>
<div class="photo" role="img" aria-label="Kitchen sink under a window" style="left:0;top:1619px;width:282px;height:215px;background:linear-gradient(135deg,#7c808a,#b9bcc2 55%,#ededee)"></div>
<div class="photo overlay" role="img" aria-label="Dark kitchen with pendant light and range hood" style="left:305px;top:1382px;width:283px;height:452px;background:linear-gradient(180deg,#4a4a4a,#383838 60%,#2e2e2e)"></div>
<div class="abs serif" style="left:323px;top:1727px;font-size:17px;color:var(--white)">Project Title</div>
<div class="abs" style="left:323px;top:1763px;width:250px;font-size:12.5px;line-height:16px;color:var(--white)">Lorem Ipsum is simply dummy text types setting in the industry.</div>
<svg class="abs" style="left:324px;top:1805px" width="14" height="14" viewBox="0 0 14 14"><circle cx="7" cy="7" r="6" fill="none" stroke="#fff" stroke-width="1.2"/><path d="M4 7h6M7.5 4.5L10 7 7.5 9.5" fill="none" stroke="#fff" stroke-width="1.2"/></svg>
<div class="photo" role="img" aria-label="White kitchen with grey island and chandelier" style="left:611px;top:1382px;width:284px;height:215px;background:linear-gradient(135deg,#eef0f1,#c8ccd0 55%,#56606b)"></div>
<div class="photo" role="img" aria-label="Kitchen island with grey cabinets and pendant lights" style="left:611px;top:1619px;width:284px;height:215px;background:linear-gradient(135deg,#d6cfc2,#8f8778 55%,#4b4c50)"></div>
<div class="photo" role="img" aria-label="Long bathroom with freestanding tub and striped floor" style="left:918px;top:1382px;width:282px;height:452px;background:linear-gradient(160deg,#f3f4f5,#d6dade 50%,#8d96a0)"></div>
<div class="btn" style="left:530px;top:1872px;width:146px;height:36px">View More</div>

<!-- about -->
<h2 class="section-title" style="top:1950px;font-weight:400">About us</h2>
<div class="rule" style="left:581px;top:2000px"></div>
<div class="photo" role="img" aria-label="Bright hallway with plant" style="left:113px;top:2020px;width:226px;height:214px;background:linear-gradient(135deg,#a7acaf,#eef0f0 55%,#9aa19a)"></div>
<div class="photo" role="img" aria-label="Kitchen with chandelier" style="left:352px;top:2065px;width:132px;height:83px;background:linear-gradient(135deg,#d4d8db,#8a9096)"></div>
<div class="frame" style="left:496px;top:2119px;width:28px;height:28px"></div>
<div class="photo" role="img" aria-label="Living room with cushions" style="left:183px;top:2247px;width:169px;height:106px;background:linear-gradient(135deg,#51555a,#8e8578 55%,#c9beb0)"></div>
<div class="photo" role="img" aria-label="Kitchen island with dark wood cabinets" style="left:352px;top:2161px;width:226px;height:216px;background:linear-gradient(135deg,#8a8a86,#5e564d 55%,#2f3e63);outline:5px solid #fff"></div>
<div class="frame" style="left:141px;top:2248px;width:29px;height:29px"></div>

<h3 class="abs serif" style="left:627px;top:2055px;width:470px;font-weight:400;font-size:30px;line-height:32px">Our 30th Year in the Kitchen and Bath Industry!</h3>
<p class="about-p" style="top:2133px">Lorem Ipsum is simply dummy text of the printing and typesetting industry has been the industry's standard dummy text ever since the 1500s,</p>
<p class="about-p" style="top:2179px">when an unknown printer took a galley of type and scrambled it to make a type specimen book. It has survived not only five centuries, but also the leap into elect ronic typesetting, remaining essentially unchanged. It was popularised industries are in the 1960s</p>
<p class="about-p" style="top:2255px">with the release of Presstype sheets containing Lorem Ipsum passages, and more recently with desktop publishing software like Quire Layout including ipsum text versions of Lorem Ipsum.</p>
<div class="btn" style="left:629px;top:2321px;width:146px;height:36px">Read More</div>

<!-- testimonials -->
<h2 class="abs serif" style="left:110px;top:2505px;font-weight:400;font-size:34px">What Clients Say About Us</h2>
<div class="abs serif" style="left:200px;top:2555px;width:190px;text-align:center;font-size:14px">Testimonials</div>
<p class="abs" style="left:110px;top:2603px;width:470px;font-size:12px;line-height:15.3px;color:var(--ink)">Harborline Kitchens Inc. had done an awesome remodeling of my wife's kitchen several years ago so I called on them to remodel my bathroom as it was in need of a lot of work. Sam and his crew of professionals came in and did an amazing job. Sam and his wife helped pick out just the right vanity, knobs, countertop and flooring to match. They coordinated the carpenter, plumber, electrician and plaster. He kept in contact throughout the whole remodeling process. If you're looking to get an excellent remodeling at a reasonable price call Harborline Kitchens you will not be disappointed.</p>
<div class="abs sans" style="left:111px;top:2746px;font-size:15px;color:var(--ink)">Mara Ellison</div>
<div class="abs" style="left:110px;top:2772px;font-size:12px;letter-spacing:3px;color:var(--star)">★★★★★</div>
<div class="dot" style="left:112px;top:2808px;background:var(--ink)"></div>
<div class="dot" style="left:125px;top:2808px;background:#999"></div>
<div class="dot" style="left:138px;top:2808px;background:#999"></div>

<!-- quote -->
<div class="abs" style="left:624px;top:2494px;width:463px;height:381px;background:var(--panel)"></div>
<h2 class="abs serif" style="left:657px;top:2522px;font-weight:400;font-size:33px">Get A Free Quote</h2>
<div class="field" style="left:657px;top:2571px;width:193px;height:40px">Name*</div>
<div class="field" style="left:864px;top:2571px;width:193px;height:40px">Phone*</div>
<div class="field" style="left:657px;top:2625px;width:193px;height:40px">Email*</div>
<div class="field" style="left:864px;top:2625px;width:193px;height:40px">Subject*</div>
<div class="field" style="left:657px;top:2677px;width:400px;height:108px">Message</div>
<div class="btn" style="left:657px;top:2801px;width:146px;height:36px">Send Now</div>

<!-- footer -->
<svg class="abs" style="left:0;top:2900px" width="1200" height="376" viewBox="0 0 1200 376">
  <path d="M0 60 C250 35 450 0 700 12 C900 22 1050 25 1200 0 L1200 376 L0 376 Z" fill="#000"/>
</svg>
<div class="abs" style="left:114px;top:3008px;display:flex;align-items:center;gap:8px">
  <div style="width:48px;height:48px;border:2px solid #fff;border-radius:50%"></div>
  <div style="font-family:'Marcellus',serif;color:#fff;line-height:1.05">
    <div style="font-size:19px">HARBORLINE</div>
    <div style="font-size:10px">KITCHEN AND BATH, INC</div>
    <div style="font-size:6px;letter-spacing:2px">COMMITTED TO QUALITY</div>
  </div>
</div>
<p class="abs" style="left:114px;top:3062px;width:250px;font-size:12px;line-height:14.5px;color:var(--white)">Lorem Ipsum is simply dummy text of the printing and typesetting industry has been the industry's standard.</p>
<div class="abs" style="left:114px;top:3122px;font-size:12px;color:var(--white);text-decoration:underline">Read More</div>

<div class="footer-h" style="left:458px">Quick Links</div>
<div class="footer-rule" style="left:458px"></div>
<div class="flink" style="top:3063px"><span>&gt;</span>Home</div>
<div class="flink" style="top:3085px"><span>&gt;</span>About us</div>
<div class="flink" style="top:3108px"><span>&gt;</span>Our Services</div>
<div class="flink" style="top:3131px"><span>&gt;</span>Projects</div>
<div class="flink" style="top:3154px"><span>&gt;</span>Contact us</div>

<div class="footer-h" style="left:648px">Contact info</div>
<div class="footer-rule" style="left:648px"></div>
<svg class="abs" style="left:650px;top:3066px" width="12" height="12" viewBox="0 0 12 12"><path d="M2 1l2.5 0 1 3-1.5 1c.8 1.6 1.6 2.4 3 3l1-1.5 3 1V11c-5 .5-9.5-4-9-10z" fill="#fff"/></svg>
<div class="fline" style="top:3063px">555-014-2290</div>
<svg class="abs" style="left:650px;top:3089px" width="12" height="10" viewBox="0 0 12 10"><rect x="0.5" y="0.5" width="11" height="9" fill="none" stroke="#fff"/><path d="M0.5 0.5L6 5.5 11.5 0.5" fill="none" stroke="#fff"/></svg>
<div class="fline" style="top:3085px">hello@harborlinekb.example</div>
<svg class="abs" style="left:651px;top:3109px" width="10" height="14" viewBox="0 0 10 14"><path d="M5 0a5 5 0 0 1 5 5c0 3.5-5 9-5 9S0 8.5 0 5a5 5 0 0 1 5-5z" fill="#fff"/><circle cx="5" cy="5" r="1.8" fill="#000"/></svg>
<div class="fline" style="top:3108px">48 Linden Ave.</div>
<div class="fline" style="top:3131px">Maple Grove, NY 10000</div>

<div class="footer-h" style="left:904px">Our Newsletter</div>
<div class="footer-rule" style="left:904px"></div>
<div class="abs" style="left:902px;top:3071px;width:185px;height:35px;border:1.5px solid #fff;border-radius:18px;color:#fff;font-size:12px;padding:9px 14px">Your Email</div>
<div class="abs" style="left:902px;top:3117px;width:185px;height:36px;background:#fff;border-radius:18px;color:#000;font-size:12px;display:flex;align-items:center;justify-content:center">Subscribe Now</div>

<div class="abs" style="left:114px;top:3209px;width:973px;height:1px;background:#fff"></div>
<div class="abs" style="left:114px;top:3226px;font-size:12px;color:var(--white)">Copyright © 2020 HARBORLINE . All Right Reserved</div>
<div class="social" style="left:970px"></div>
<div class="social" style="left:1002px"></div>
<div class="social" style="left:1033px"></div>
<div class="social" style="left:1064px"></div>

</body>
</html>
```